Beauty Therapy Web Design

I need a web page design for a small beauty therapy clinic, the owner is currently the only beauty therapist working there.
We require the following pages:
Home
About
Treatments
Nails
Courses
Contact
I will attach the clinics business card, treatment menu and signage so that you get a feeling for the branding colours etc.
This is the first website for the beauty therapist, she would like to attract new clients and also tourists that come in on the cruise ships. The thing that sets her apart from other clinics is that she welcomes texting for appointments.
I have selected refundable because I have never done this before so I don't know what to expect, I have the full intention of going through with it as long as I get a good design.
Feel free to ask for further information
Reason: Project extended as I am away for work and am unable to meet with the owner.
Target Market(s)
Females 18 to 50
Industry/Entity Type
Business
Look and feel
Each slider illustrates characteristics of the customer's brand and the style your logo design should communicate.

```html
<!DOCTYPE html>
<html lang="en">
<head>
<meta charset="utf-8">
<title>Lumera Beauty Therapy</title>
<link href="https://fonts.googleapis.com/css2?family=Arimo:wght@400;700&display=swap" rel="stylesheet">
<style>
:root{
  --brand:#4a2fb0;
  --ink:#2b2b2b;
  --muted:#6b6b6b;
  --heading:#1f3440;
  --contact:#4b3f7a;
  --nav:#000;
  --footer:#232323;
  --panel:#ffffff;
  --rule:#dcdcdc;
  --link:#2f2a5c;
  --bullet:#2a9aa6;
  --dot:#6a4bd8;
}
*{margin:0;padding:0;box-sizing:border-box}
html,body{width:979px;height:1200px;overflow:hidden}
body{font-family:"Arimo",Arial,sans-serif;background:linear-gradient(#fafafa,#e9e9e9 600px,#efefef);position:relative;color:var(--ink)}
.footer-band{position:absolute;left:0;top:1028px;width:979px;height:172px;background:var(--footer)}
.brand{position:absolute;left:83px;top:32px;color:var(--brand);font-weight:700;line-height:1}
.brand .name{font-size:74px;letter-spacing:-1px}
.brand .sub{font-size:33px;margin-top:10px;letter-spacing:1px}
.contact{position:absolute;right:86px;top:50px;text-align:right;color:var(--contact);font-size:13px;line-height:23px}
.contact b{font-weight:400;font-size:16px;margin-left:4px}
.nav{position:absolute;left:38px;top:166px;width:903px;height:24px;background:var(--nav)}
.nav a{position:absolute;top:0;height:24px;line-height:24px;color:#fff;font-size:12px;font-weight:700;text-decoration:none;text-align:center;border-left:1px solid #555}
.nav a:last-child{border-right:1px solid #555}
.hero{position:absolute;left:38px;top:213px;width:903px;height:365px;border:1px solid #a9a3e6;background:linear-gradient(100deg,#f1eef4 0%,#f3d9cc 35%,#eec0a6 55%,#e8b48e 70%,#f4eee9 100%)}
.hero-shadow{position:absolute;left:62px;top:578px;width:855px;height:25px;background:linear-gradient(#333,rgba(0,0,0,.05));filter:blur(3px);border-radius:0 0 8px 8px}
.dots{position:absolute;left:455px;top:618px;display:flex;gap:6px}
.dots span{width:19px;height:19px;border-radius:50%;background:radial-gradient(circle at 40% 35%,#9d86f0,var(--dot) 60%,#4a2fb0)}
.dots span:first-child{background:radial-gradient(circle at 40% 35%,#f1ecff,#b9a8f3)}
.panel{position:absolute;left:38px;top:657px;width:903px;height:412px;background:var(--panel);border-radius:4px}
h2{font-weight:400;font-size:19px;color:var(--heading);position:absolute}
p{font-size:12.5px;line-height:18.4px;color:var(--muted);position:absolute}
.lead{color:var(--ink);font-weight:700}
.more{position:absolute;font-size:13px;font-weight:700;color:var(--link);text-decoration:none}
.rule{position:absolute;left:65px;top:898px;width:328px;height:1px;background:var(--rule)}
.video{position:absolute;left:422px;top:679px;width:327px;height:182px;border:1px solid #bbb;background:linear-gradient(90deg,#f2d9d9,#f5e7dd 45%,#e6d4c4 60%,#3a3230 90%)}
.controls{position:absolute;left:6px;bottom:6px;right:6px;height:24px;display:flex;align-items:center;gap:6px}
.controls .play{width:42px;height:24px;background:#2b2b2b;display:flex;align-items:center;justify-content:center}
.controls .bar{flex:1;height:22px;background:rgba(30,30,30,.85);color:#ddd;font-size:8px;display:flex;align-items:center;gap:6px;padding:0 6px}
.controls .track{flex:1;height:3px;background:#777}
.side-list{position:absolute;left:783px;top:711px;width:115px;list-style:none}
.side-list li{height:31.7px;line-height:31px;border-bottom:1px solid #e3e3e3;font-size:12.5px;color:var(--ink);padding-left:32px;position:relative}
.side-list li:last-child{border-bottom:none}
.side-list li::before{content:"";position:absolute;left:18px;top:12px;width:7px;height:7px;border-radius:50%;background:var(--bullet);box-shadow:0 0 0 1px #9fd6db}
.site-footer{position:absolute;left:0;top:1100px;width:979px;text-align:center;color:#fff;font-size:12.5px;line-height:23px}
</style>
</head>
<body>
<div class="footer-band"></div>

<header>
  <div class="brand"><div class="name">Lumera</div><div class="sub">BEAUTY THERAPY</div></div>
  <div class="contact">
    <div>Phone Celia <b>07 555 0142</b></div>
    <div>Cellphone <b>027 555 0198</b></div>
    <div>Cnr Kowhai St. &amp; Harbour Rd, Seacliff Bay</div>
  </div>
</header>

<nav class="nav">
  <a href="#" style="left:126px;width:90px">HOME</a>
  <a href="#" style="left:216px;width:99px">ABOUT</a>
  <a href="#" style="left:315px;width:136px">TREATMENTS</a>
  <a href="#" style="left:451px;width:90px">NAILS</a>
  <a href="#" style="left:541px;width:123px">COURSES</a>
  <a href="#" style="left:664px;width:113px">CONTACT</a>
</nav>

<div class="hero" role="img" aria-label="Photo of a manicurist painting a client's nails with red polish"></div>
<div class="hero-shadow"></div>
<div class="dots"><span></span><span></span><span></span><span></span></div>

<main class="panel"></main>

<h2 style="left:65px;top:679px">Eu eam detracto repudiare</h2>
<p class="lead" style="left:66px;top:721px;width:330px">Cu ceteros dissentiunt vix, at eos assum melius volumus. Nec et erant clita consul, ius eu mazim</p>
<p style="left:66px;top:774px;width:330px">Cu ceteros dissentiunt vix, at eos assum melius volumus. Nec et erant clita consul, ius eu mazim nullam euripidis, his velit percipit et. Eam mundi prompta ad, option apeirian vivendum ei ius, his option lobortis eu. In natum nullam volumus mel, vim ne albucius assueverit. Duo ea errem invidunt persequeris.</p>
<div class="rule"></div>
<p style="left:66px;top:918px;width:330px">Cu ceteros dissentiunt vix, at eos assum melius volumus. Nec et erant clita consul, ius eu mazim nullam euripidis, his velit percipit et. Eam mundi prompta ad, option apeirian vivendum ei ius, his option lobortis eu. In natum nullam volumus mel, vim ne albucius assueverit. Duo ea errem invidunt persequeris.</p>
<a class="more" href="#" style="left:65px;top:1038px">Read more</a>

<div class="video" role="img" aria-label="Video still of a nail technician working with a client">
  <div class="controls">
    <div class="play"><svg width="10" height="11" viewBox="0 0 10 11"><path d="M1 0l9 5.5L1 11z" fill="#ddd"/></svg></div>
    <div class="bar"><span>00:00</span><span class="track"></span><span>01:00</span></div>
  </div>
</div>
<h2 style="left:422px;top:881px">Eu eam detracto repudiare</h2>
<p style="left:423px;top:918px;width:330px">Cu ceteros dissentiunt vix, at eos assum melius volumus. Nec et erant clita consul, ius eu mazim nullam euripidis, his velit percipit et. Eam mundi prompta ad, option apeirian vivendum ei ius, his option lobortis eu. In natum nullam volumus mel, vim ne albucius assueverit. Duo ea errem invidunt persequeris.</p>
<a class="more" href="#" style="left:422px;top:1038px">Read more</a>

<h2 style="left:783px;top:679px">Eu eam detracto</h2>
<ul class="side-list">
  <li>Reformidans</li><li>Iuvaret</li><li>Consequuntur</li><li>Ullamcorper</li><li>Essent</li>
  <li>Gloriatur</li><li>Dicam</li><li>Primis</li><li>Scriptorem</li><li>Nulla</li>
</ul>

<footer class="site-footer">
  <div>Copyright 2012 Lumera Beauty Therapy</div>
  <div>Phone Celia 07 555 0142 &nbsp;&nbsp; Cellphone 027 555 0198</div>
  <div>Cnr Kowhai St. &amp; Harbour Rd, Seacliff Bay</div>
</footer>
</body>
</html>
```